Business card for Cat Cafe

I have started a small business and need a business card designed. The business is a cat cafe, that is, an ordinary cafe that serves coffee and snacks but with a twist - you can bring your cat to play. In fact the idea is to encourage everyone to come and bring your feline friend in order to build community and provide some fun and connections between fellow cat lovers. Themes of the business include;

- Fun
- Discovery
- Connections

The name of the cafe is Brews and Whiskers!

We look forward to seeing what creative ideas you may have!
Updates

Hi,

 Please note the contact details as below;
14 Tarrant Lane, Marlow Vale,
Harbourton, WR
3071

Target Market(s)

Cat owners, any age group

Industry/Entity Type

Small Business

Requirements
Must have
• Must include some type of imagery of a cat itself.

```html
<!DOCTYPE html>
<html lang="en">
<head>
<meta charset="utf-8">
<title>Brews &amp; Whiskers — Business Card</title>
<link rel="stylesheet" href="https://fonts.googleapis.com/css2?family=Quicksand:wght@400&family=Cousine:wght@400;700&display=swap">
<style>
  :root {
    --backdrop: #efeee9;
    --card-light: #cfd36a;
    --card-mid: #c2c756;
    --card-deep: #b4b948;
    --band: #3b3820;
    --ink-light: #ece8d4;
    --ink-soft: #d9d5bd;
    --ink-dark: #3a3a22;
    --mark-fill: #a8865e;
  }
  html, body {
    margin: 0;
    width: 1200px;
    height: 876px;
    overflow: hidden;
    background: var(--backdrop);
  }
  .canvas {
    position: relative;
    width: 1200px;
    height: 876px;
  }
  .card {
    position: absolute;
    left: 150px;
    top: 178px;
    width: 900px;
    height: 520px;
    background: linear-gradient(135deg, var(--card-light) 0%, var(--card-mid) 50%, var(--card-deep) 100%);
    box-shadow: 0 6px 18px rgba(0,0,0,0.18);
    overflow: hidden;
  }
  .card-sheen {
    position: absolute;
    inset: 0;
    background: linear-gradient(160deg, rgba(255,255,255,0.14), rgba(255,255,255,0) 60%);
  }
  .band-rule {
    position: absolute;
    left: 32px;
    right: 0;
    height: 5px;
    background: var(--band);
  }
  .band-rule--top { top: 168px; }
  .band-rule--bottom { top: 318px; }
  .band {
    position: absolute;
    left: 32px;
    right: 0;
    top: 182px;
    height: 128px;
    background: var(--band);
  }
  .brand-mark {
    position: absolute;
    left: 290px;
    top: 72px;
    display: flex;
    align-items: center;
    gap: 14px;
  }
  .brand-dot {
    width: 56px;
    height: 56px;
    border-radius: 50%;
    background: var(--mark-fill);
  }
  .brand-mark-name {
    margin: 0;
    font-family: "Quicksand", sans-serif;
    font-weight: 400;
    font-size: 26px;
    letter-spacing: 1px;
    color: var(--ink-dark);
  }
  .business-name {
    position: absolute;
    left: 0;
    right: 0;
    top: 212px;
    margin: 0;
    text-align: center;
    font-family: "Quicksand", sans-serif;
    font-weight: 400;
    font-size: 44px;
    letter-spacing: 4px;
    color: var(--ink-light);
    line-height: 1;
  }
  .business-offer {
    position: absolute;
    left: 0;
    right: 0;
    top: 266px;
    margin: 0;
    text-align: center;
    font-family: "Cousine", monospace;
    font-weight: 700;
    font-size: 18px;
    color: var(--ink-soft);
  }
  .address {
    position: absolute;
    left: 36px;
    top: 395px;
    margin: 0;
    font-family: "Cousine", monospace;
    font-size: 20px;
    line-height: 1.35;
    color: var(--ink-dark);
    font-style: normal;
  }
</style>
</head>
<body>
  <main class="canvas">
    <section class="card" aria-label="Brews and Whiskers business card">
      <div class="card-sheen"></div>
      <div class="band-rule band-rule--top"></div>
      <div class="band"></div>
      <div class="band-rule band-rule--bottom"></div>

      <div class="brand-mark">
        <span class="brand-dot"></span>
        <p class="brand-mark-name">Brews &amp; Whiskers</p>
      </div>

      <h1 class="business-name">BREWS &amp; WHISKERS</h1>
      <p class="business-offer">Coffee &amp; Snacks</p>

      <address class="address">14 Tarrant Lane, Marlow Vale,<br>Harbourton, WR<br>3071</address>
    </section>
  </main>
</body>
</html>
```